Search Fund needs a PowerPoint template design

We need a eye-catching and compelling PowerPoint design for a new company based in Chicago called Harrow Ridge Partners. We are search fund with a primary mission to acquire a founder/family/entrepreneur owned businesses (This is similar to a Private Equity firm). Our goal is to offer investors a unique avenue to invest in an attractive business acquisition while providing business owners with an alternative path to exit. We would like the design to reflect crisp and professional nature that many financial firms present. The template should build on the design of the logo including expanding a logical color palette. The presentation will be used to describe facts regarding the firm, financial data and key messaging that we want our investors and potential partners to takeaway.

Target Market(s)

Financial Investors

Industry/Entity Type

Finance

Font styles to use
Serif
Sans Serif

Colors

Designer to choose colors to be used in the design.

Requirements
Must have
• Should include cover page and slide examples. Attractive data displays (graphs, charts, infographics etc.); Compelling cover; fly pages to put in between sections; table of contents page. Needs to have white space to add text.
Should not have
• Do not redesign the logo or change the logo colors. Additional colors should be added to the PowerPoint template

```html
<!DOCTYPE html>
<html lang="en">
<head>
<meta charset="utf-8">
<title>Harrow Ridge Partners – Presentation Template</title>
<link rel="stylesheet" href="https://fonts.googleapis.com/css2?family=Lato:wght@400;700;900&display=swap">
<style>
  :root{
    --brand-blue:#1572bd;
    --brand-grey:#8f8f8f;
    --ink:#555555;
    --charcoal:#262626;
    --stage:#d0cfcf;
    --paper:#ffffff;
    --green-dark:#7fae3a;
    --green-light:#c9dc9a;
  }
  *{margin:0;padding:0;box-sizing:border-box}
  html,body{width:1200px;height:1200px;overflow:hidden;background:var(--stage)}
  body{position:relative;font-family:"Lato",sans-serif}
  .slide{position:absolute;display:block;background:var(--paper);box-shadow:0 1px 3px rgba(0,0,0,.18)}
  .slide--hero{left:353px;top:89px;width:529px;height:375px}
  .slide--cover{left:31px;top:575px;width:364px;height:273px}
  .slide--about{left:419px;top:575px;width:364px;height:273px}
  .slide--chart{left:807px;top:575px;width:364px;height:273px}
  .slide--features{left:31px;top:878px;width:364px;height:273px}
  .slide--infographic{left:419px;top:878px;width:364px;height:273px}
  .slide--closing{left:807px;top:878px;width:364px;height:273px}
  svg text{font-family:"Lato",sans-serif}
  .wordmark{fill:var(--brand-blue);font-weight:700}
  .wordmark--light{fill:var(--paper)}
  .slide-title{fill:var(--brand-blue);font-weight:700;font-size:20px}
  .tagline{fill:var(--paper);font-weight:700}
  .url{fill:var(--paper);font-weight:700;font-size:6.5px;letter-spacing:.4px}
  .page-no{fill:var(--brand-grey);font-size:9px}
  .copy{font-family:"Lato",sans-serif;color:var(--ink);font-size:8.4px;line-height:13.6px;text-align:justify}
  .copy--right{text-align:right}
  .copy h4{color:var(--brand-blue);font-size:9.5px;font-weight:700;line-height:13px}
  .tiny-label{fill:var(--brand-blue);font-weight:700;font-size:8.5px}
  .tiny-label--grey{fill:var(--brand-grey)}
  .tiny-text{fill:var(--ink);font-size:5.6px}
  .chart-num{fill:#333;font-size:4.6px}
  .thanks{fill:var(--paper);font-weight:900}
  .contact{fill:var(--paper);font-size:6.5px}
</style>
</head>
<body>

<svg width="0" height="0" style="position:absolute" aria-hidden="true">
  <defs>
    <linearGradient id="deskPhoto" x1="0" y1="0" x2="1" y2="1">
      <stop offset="0" stop-color="#e8edf2"/>
      <stop offset=".5" stop-color="#a9b4c0"/>
      <stop offset="1" stop-color="#4d5967"/>
    </linearGradient>
    <linearGradient id="meetingPhoto" x1="0" y1="0" x2="1" y2="1">
      <stop offset="0" stop-color="#e4ecf2"/>
      <stop offset=".6" stop-color="#9fa9b4"/>
      <stop offset="1" stop-color="#3a3f48"/>
    </linearGradient>
    <linearGradient id="officePhoto" x1="0" y1="0" x2="1" y2="0">
      <stop offset="0" stop-color="#6f7880"/>
      <stop offset=".45" stop-color="#c9d3dc"/>
      <stop offset="1" stop-color="#e9eef3"/>
    </linearGradient>
    <linearGradient id="tabletPhoto" x1="0" y1="0" x2="1" y2="1">
      <stop offset="0" stop-color="#2d3d55"/>
      <stop offset=".6" stop-color="#6d7682"/>
      <stop offset="1" stop-color="#b7bcc2"/>
    </linearGradient>
    <path id="hex" d="M0,-38 L33,-19 L33,19 L0,38 L-33,19 L-33,-19 Z"/>
    <symbol id="footer-band" viewBox="0 0 455 342">
      <polygon points="0,338 455,294 455,300 0,341" fill="#8f8f8f"/>
      <polygon points="0,341 455,300 455,342 0,342" fill="#1572bd"/>
    </symbol>
  </defs>
</svg>

<!-- Hero cover -->
<svg class="slide slide--hero" viewBox="0 0 661 469">
  <rect width="661" height="469" fill="var(--paper)"/>
  <polygon points="0,469 661,222 661,469" fill="var(--brand-grey)"/>
  <polygon points="0,469 661,244 661,469" fill="var(--brand-blue)"/>
  <circle cx="178" cy="244" r="192" fill="var(--brand-grey)"/>
  <g role="img" aria-label="Photo: analyst writing on financial charts at a desk">
    <circle cx="169" cy="244" r="188" fill="url(#deskPhoto)"/>
  </g>
  <text class="wordmark" x="640" y="68" text-anchor="end" font-size="42" letter-spacing="1">HARROW RIDGE</text>
  <text class="wordmark" x="560" y="90" text-anchor="middle" font-size="16" letter-spacing="6">PARTNERS</text>
  <text class="tagline" x="642" y="387" text-anchor="end" font-size="26">Lorem ipsum dolor</text>
  <text class="tagline" x="642" y="416" text-anchor="end" font-size="26">sit amet etuer met etuer.</text>
  <text class="url" x="638" y="459" text-anchor="end" font-size="9">www.harrowridgepartners.com</text>
</svg>

<!-- Slide 1: cover -->
<svg class="slide slide--cover" viewBox="0 0 455 342">
  <rect width="455" height="342" fill="var(--paper)"/>
  <polygon points="0,342 0,318 455,165 455,342" fill="var(--brand-grey)"/>
  <polygon points="0,342 0,320 455,190 455,342" fill="var(--brand-blue)"/>
  <circle cx="106" cy="178" r="138" fill="var(--brand-grey)"/>
  <g role="img" aria-label="Photo: analyst writing on financial charts at a desk">
    <circle cx="100" cy="178" r="135" fill="url(#deskPhoto)"/>
  </g>
  <text class="wordmark" x="441" y="51" text-anchor="end" font-size="30" letter-spacing=".5">HARROW RIDGE</text>
  <text class="wordmark" x="362" y="67" text-anchor="middle" font-size="11.5" letter-spacing="4">PARTNERS</text>
  <text class="tagline" x="441" y="283" text-anchor="end" font-size="18">Lorem ipsum dolor</text>
  <text class="tagline" x="441" y="303" text-anchor="end" font-size="18">sit amet etuer met etuer.</text>
  <text class="url" x="439" y="335" text-anchor="end">www.harrowridgepartners.com</text>
</svg>

<!-- Slide 2: about us -->
<svg class="slide slide--about" viewBox="0 0 455 342">
  <rect width="455" height="342" fill="var(--paper)"/>
  <text class="slide-title" x="23" y="34">ABOUT US</text>
  <line x1="136" y1="28" x2="214" y2="28" stroke="var(--brand-grey)" stroke-width="1.2"/>
  <foreignObject x="21" y="52" width="414" height="72">
    <div xmlns="http://www.w3.org/1999/xhtml" class="copy">Lorem ipsum dolor sit amet, consectetuer adipiscing elit, sed diam nonummy nibh euismod tincidunt ut laoreet dolore magna aliquam erat volutpat. Ut wisi enim ad minim veniam, quis nostrud exerci tation ullamcorper suscipit lobortis nisl ut aliquip ex ea commodo consequat. Duis autem vel eum iriure dolor in hendrerit in vulputate velit esse molestie consequat, vel illum dolore eu feugiat nulla facilisis.</div>
  </foreignObject>
  <circle cx="108" cy="224" r="91" fill="none" stroke="var(--brand-blue)" stroke-width="1"/>
  <g role="img" aria-label="Photo: business meeting between two colleagues">
    <circle cx="108" cy="224" r="88" fill="url(#meetingPhoto)"/>
  </g>
  <foreignObject x="185" y="140" width="248" height="140">
    <div xmlns="http://www.w3.org/1999/xhtml" class="copy copy--right">Lorem ipsum dolor sit amet, consectetuer adipiscing elit, sed diam nonummy nibh euismod tincidunt ut laoreet dolore magna aliquam erat volutpat. Ut wisi enim ad minim veniam, quis nostrud exerci tation ullamcorper the is suscipit lobortis nisl ut aliquip ex ea commodo lorem consequat. Duis autem vel eum iriure dolor in this i hendrerit in vulputate velit esse molestie cons vel illum dolore eu feugiat nulla facilisishendrerit lorem ipsum in vulputate velit esse molestie cons vel illum dolore eu feugiat nulla facilisis..</div>
  </foreignObject>
  <use href="#footer-band" x="0" y="0" width="455" height="342"/>
  <text class="page-no" x="11" y="334">2.</text>
  <text class="url" x="436" y="329" text-anchor="end">www.harrowridgepartners.com</text>
</svg>

<!-- Slide 3: chart -->
<svg class="slide slide--chart" viewBox="0 0 455 342">
  <rect width="455" height="342" fill="var(--paper)"/>
  <text class="slide-title" x="18" y="34">LOREM IPSUM</text>
  <line x1="166" y1="28" x2="244" y2="28" stroke="var(--brand-grey)" stroke-width="1.2"/>
  <foreignObject x="18" y="52" width="422" height="60">
    <div xmlns="http://www.w3.org/1999/xhtml" class="copy">Lorem ipsum dolor sit amet, consectetuer adipiscing elit, sed diam nonummy nibh euismod tincidunt ut laoreet dolore magna aliquam erat volutpat. Ut wisi enim ad minim veniam, quis nostrud exerci tation ullamcorper suscipit lobortis nisl ut aliquip ex ea commodo consequat. Duis autem vel eum iriure dolor in hendrerit in vulputate velit esse molestie.</div>
  </foreignObject>
  <foreignObject x="17" y="117" width="180" height="170">
    <div xmlns="http://www.w3.org/1999/xhtml" class="copy">Lorem ipsum dolor sit amet, consectetuer adipiscing elit, sed diam nonummy nibh euismod tincidunt ut laoreet dolore magna aliquam erat volutpat. Ut wisi enim ad minim veniam, quis nostrud exerci tation ullamcorper suscipit lobortis nisl ut aliquip ex ea commodo consequat. Duis autem vel eum iriure dolor in hendrerit in vulputate velit lorem is thwavh desse molestie.adipiscing elit, sed diam nonummy nibh euismod tincidunt ut laoreet dolore magna aliquam erat</div>
  </foreignObject>
  <g class="bar-chart">
    <rect x="205" y="122" width="230" height="132" fill="var(--paper)" stroke="#bdbdbd" stroke-width=".6"/>
    <line x1="210" y1="229" x2="372" y2="229" stroke="#999" stroke-width=".5"/>
    <g fill="var(--green-light)">
      <rect x="213" y="213.6" width="8" height="15.4"/>
      <rect x="226" y="203.8" width="8" height="25.2"/>
      <rect x="239" y="188.4" width="8" height="40.6"/>
      <rect x="252" y="176.3" width="8" height="52.7"/>
      <rect x="265" y="163.8" width="8" height="65.2"/>
      <rect x="278" y="171.3" width="8" height="57.7"/>
      <rect x="291" y="155.6" width="8" height="73.4"/>
      <rect x="304" y="151.5" width="8" height="77.5"/>
      <rect x="317" y="150.6" width="8" height="78.4"/>
      <rect x="330" y="153.2" width="8" height="75.8"/>
      <rect x="343" y="138.6" width="8" height="90.4"/>
      <rect x="356" y="133.5" width="8" height="95.5"/>
    </g>
    <g fill="var(--green-dark)">
      <rect x="213" y="214" width="8" height="15"/>
      <rect x="226" y="207" width="8" height="22"/>
      <rect x="239" y="201" width="8" height="28"/>
      <rect x="252" y="196" width="8" height="33"/>
      <rect x="265" y="191" width="8" height="38"/>
      <rect x="278" y="193" width="8" height="36"/>
      <rect x="291" y="191" width="8" height="38"/>
      <rect x="304" y="188" width="8" height="41"/>
      <rect x="317" y="189" width="8" height="40"/>
      <rect x="330" y="191" width="8" height="38"/>
      <rect x="343" y="185" width="8" height="44"/>
      <rect x="356" y="189" width="8" height="40"/>
    </g>
    <g fill="#555">
      <rect x="213" y="212" width="8" height="1.6"/><rect x="226" y="202.2" width="8" height="1.6"/>
      <rect x="239" y="186.8" width="8" height="1.6"/><rect x="252" y="174.7" width="8" height="1.6"/>
      <rect x="265" y="162.2" width="8" height="1.6"/><rect x="278" y="169.7" width="8" height="1.6"/>
      <rect x="291" y="154" width="8" height="1.6"/><rect x="304" y="149.9" width="8" height="1.6"/>
      <rect x="317" y="149" width="8" height="1.6"/><rect x="330" y="151.6" width="8" height="1.6"/>
      <rect x="343" y="137" width="8" height="1.6"/><rect x="356" y="131.9" width="8" height="1.6"/>
    </g>
    <g class="chart-num" text-anchor="middle">
      <text x="217" y="209">32.0</text><text x="230" y="199">52.6</text><text x="243" y="184">84.5</text>
      <text x="256" y="172">109.8</text><text x="269" y="160">135.8</text><text x="282" y="167">120.2</text>
      <text x="295" y="151">152.9</text><text x="308" y="147">161.4</text><text x="321" y="146">163.3</text>
      <text x="334" y="149">158.0</text><text x="347" y="134">188.4</text><text x="360" y="129">199.0</text>
    </g>
    <g class="chart-num" text-anchor="middle">
      <text x="217" y="236">2004</text><text x="230" y="236">2005</text><text x="243" y="236">2006</text>
      <text x="256" y="236">2007</text><text x="269" y="236">2008</text><text x="282" y="236">2009</text>
      <text x="295" y="236">2010</text><text x="308" y="236">2011</text><text x="321" y="236">2012</text>
      <text x="334" y="236">2013</text><text x="347" y="236">2014</text><text x="360" y="236">2015</text>
    </g>
    <rect x="389" y="187" width="3" height="3" fill="#555"/>
    <text class="chart-num" x="394" y="190">Bond/other</text>
    <rect x="389" y="199" width="3" height="3" fill="var(--green-light)"/>
    <text class="chart-num" x="394" y="202">Project finance</text>
    <rect x="389" y="211" width="3" height="3" fill="var(--green-dark)"/>
    <text class="chart-num" x="394" y="214">Balance sheet</text>
  </g>
  <use href="#footer-band" x="0" y="0" width="455" height="342"/>
  <text class="page-no" x="11" y="334">3.</text>
  <text class="url" x="436" y="329" text-anchor="end">www.harrowridgepartners.com</text>
</svg>

<!-- Slide 4: features -->
<svg class="slide slide--features" viewBox="0 0 455 342">
  <rect width="455" height="342" fill="var(--paper)"/>
  <text class="slide-title" x="21" y="33">LOREM IPSUM</text>
  <line x1="169" y1="27" x2="247" y2="27" stroke="var(--brand-grey)" stroke-width="1.2"/>
  <g role="img" aria-label="Photo: blurred office team behind a row of finance icons">
    <rect x="0" y="46" width="455" height="116" fill="url(#officePhoto)"/>
  </g>
  <foreignObject x="21" y="176" width="200" height="135">
    <div xmlns="http://www.w3.org/1999/xhtml" class="copy" style="text-align:left">
      <h4>Sub Title-2</h4>
      <p>Lorem ipsum dolor sit amet, etuer.Lorem ipsum dolor sit amet, etuer.Lorem ipsum dolor sit amet, etuer.</p>
      <h4 style="margin-top:6px">Sub Title-3</h4>
      <p>Lorem ipsum dolor sit amet, etuer.Lorem ipsum dolor sit amet, etuer.Lorem ipsum dolor sit amet, etuer.</p>
    </div>
  </foreignObject>
  <foreignObject x="246" y="176" width="200" height="135">
    <div xmlns="http://www.w3.org/1999/xhtml" class="copy" style="text-align:left">
      <h4>Sub Title-2</h4>
      <p>Lorem ipsum dolor sit amet, etuer.Lorem ipsum dolor sit amet, etuer.Lorem ipsum dolor sit amet, etuer sit amet, etuer.</p>
      <h4 style="margin-top:6px">Sub Title-3</h4>
      <p>Lorem ipsum dolor sit amet, etuer.Lorem ipsum dolor sit amet, etuer.Lorem ipsum dolor sit amet, etuer sit amet etuer.</p>
    </div>
  </foreignObject>
  <use href="#footer-band" x="0" y="0" width="455" height="342"/>
  <text class="page-no" x="11" y="334">4.</text>
  <text class="url" x="436" y="329" text-anchor="end">www.harrowridgepartners.com</text>
</svg>

<!-- Slide 5: infographic -->
<svg class="slide slide--infographic" viewBox="0 0 455 342">
  <rect width="455" height="342" fill="var(--paper)"/>
  <text class="slide-title" x="22" y="29">LOREM IPSUM</text>
  <line x1="170" y1="23" x2="248" y2="23" stroke="var(--brand-grey)" stroke-width="1.2"/>
  <g class="hex-grid">
    <use href="#hex" x="153" y="106" fill="var(--brand-blue)"/>
    <use href="#hex" x="226" y="106" fill="var(--brand-grey)"/>
    <use href="#hex" x="300" y="106" fill="var(--brand-blue)"/>
    <use href="#hex" x="116" y="173" fill="var(--brand-grey)"/>
    <use href="#hex" x="190" y="173" fill="var(--brand-blue)"/>
    <use href="#hex" x="264" y="173" fill="var(--brand-grey)"/>
    <use href="#hex" x="336" y="173" fill="var(--brand-blue)"/>
    <use href="#hex" x="153" y="240" fill="var(--brand-blue)"/>
    <use href="#hex" x="226" y="240" fill="var(--brand-grey)"/>
    <use href="#hex" x="300" y="240" fill="var(--brand-blue)"/>
  </g>
  <g class="hex-icons" fill="var(--paper)">
    <!-- bank -->
    <polygon points="141,100 153,92 165,100"/><rect x="142" y="102" width="22" height="13" rx="1"/>
    <text x="153" y="113" font-size="10" font-weight="900" text-anchor="middle" fill="var(--brand-blue)">$</text>
    <polygon points="250,166 262,158 274,166"/><rect x="251" y="168" width="22" height="13" rx="1"/>
    <text x="262" y="179" font-size="10" font-weight="900" text-anchor="middle" fill="var(--brand-grey)">$</text>
    <!-- card -->
    <rect x="213" y="97" width="26" height="18" rx="2"/><rect x="213" y="101" width="26" height="3" fill="var(--brand-grey)"/>
    <rect x="323" y="164" width="26" height="18" rx="2"/><rect x="323" y="168" width="26" height="3" fill="var(--brand-blue)"/>
    <!-- settings box -->
    <rect x="290" y="96" width="20" height="20" rx="2"/><circle cx="300" cy="106" r="4" fill="var(--brand-blue)"/>
    <rect x="143" y="230" width="20" height="20" rx="2"/><circle cx="153" cy="240" r="4" fill="var(--brand-blue)"/>
    <!-- bars -->
    <rect x="105" y="174" width="4" height="8"/><rect x="111" y="169" width="4" height="13"/><rect x="117" y="164" width="4" height="18"/><rect x="123" y="160" width="4" height="22"/>
    <rect x="215" y="241" width="4" height="8"/><rect x="221" y="236" width="4" height="13"/><rect x="227" y="231" width="4" height="18"/><rect x="233" y="227" width="4" height="22"/>
    <!-- money bag -->
    <circle cx="190" cy="177" r="11"/><polygon points="184,163 196,163 192,168 188,168"/>
    <text x="190" y="181" font-size="12" font-weight="900" text-anchor="middle" fill="var(--brand-blue)">$</text>
    <circle cx="300" cy="244" r="11"/><polygon points="294,230 306,230 302,235 298,235"/>
    <text x="300" y="248" font-size="12" font-weight="900" text-anchor="middle" fill="var(--brand-blue)">$</text>
  </g>
  <g class="hex-labels">
    <text class="tiny-label" x="50" y="63">Lorem Ipsum</text>
    <line x1="50" y1="67" x2="107" y2="67" stroke="var(--brand-blue)" stroke-width=".6"/>
    <text class="tiny-text" x="50" y="77">Lorem ipsum this is</text><text class="tiny-text" x="50" y="84">lorem text.</text>

    <text class="tiny-label tiny-label--grey" x="237" y="45" text-anchor="middle">Lorem Ipsum</text>
    <text class="tiny-text" x="237" y="59" text-anchor="middle">Lorem ipsum this is</text><text class="tiny-text" x="237" y="66" text-anchor="middle">lorem text.</text>

    <text class="tiny-label" x="430" y="60" text-anchor="end">Lorem Ipsum</text>
    <line x1="373" y1="64" x2="430" y2="64" stroke="var(--brand-blue)" stroke-width=".6"/>
    <text class="tiny-text" x="430" y="74" text-anchor="end">Lorem ipsum this is</text><text class="tiny-text" x="430" y="81" text-anchor="end">lorem text.</text>

    <text class="tiny-label" x="430" y="122" text-anchor="end">Lorem Ipsum</text>
    <line x1="373" y1="126" x2="430" y2="126" stroke="var(--brand-blue)" stroke-width=".6"/>
    <text class="tiny-text" x="430" y="136" text-anchor="end">Lorem ipsum this is</text><text class="tiny-text" x="430" y="143" text-anchor="end">lorem text.</text>

    <text class="tiny-label tiny-label--grey" x="20" y="137">Lorem Ipsum</text>
    <line x1="20" y1="141" x2="77" y2="141" stroke="var(--brand-grey)" stroke-width=".6"/>
    <text class="tiny-text" x="20" y="151">Lorem ipsum this is</text><text class="tiny-text" x="20" y="158">lorem text.</text>

    <text class="tiny-label" x="46" y="216">Lorem Ipsum</text>
    <line x1="46" y1="220" x2="103" y2="220" stroke="var(--brand-blue)" stroke-width=".6"/>
    <text class="tiny-text" x="46" y="230">Lorem ipsum this is</text><text class="tiny-text" x="46" y="237">lorem text.</text>

    <text class="tiny-label" x="430" y="213" text-anchor="end">Lorem Ipsum</text>
    <line x1="373" y1="217" x2="430" y2="217" stroke="var(--brand-blue)" stroke-width=".6"/>
    <text class="tiny-text" x="430" y="227" text-anchor="end">Lorem ipsum this is</text><text class="tiny-text" x="430" y="234" text-anchor="end">lorem text.</text>

    <text class="tiny-label" x="76" y="276">Lorem Ipsum</text>
    <line x1="76" y1="280" x2="133" y2="280" stroke="var(--brand-blue)" stroke-width=".6"/>
    <text class="tiny-text" x="76" y="290">Lorem ipsum this is</text><text class="tiny-text" x="76" y="297">lorem text.</text>

    <text class="tiny-label tiny-label--grey" x="200" y="285">Lorem Ipsum</text>
    <line x1="200" y1="289" x2="257" y2="289" stroke="var(--brand-grey)" stroke-width=".6"/>
    <text class="tiny-text" x="200" y="299">Lorem ipsum this is</text><text class="tiny-text" x="200" y="306">lorem text.</text>

    <text class="tiny-label tiny-label--grey" x="318" y="277">Lorem Ipsum</text>
    <line x1="318" y1="281" x2="375" y2="281" stroke="var(--brand-grey)" stroke-width=".6"/>
    <text class="tiny-text" x="318" y="291">Lorem ipsum this is</text><text class="tiny-text" x="318" y="298">lorem text.</text>
  </g>
  <use href="#footer-band" x="0" y="0" width="455" height="342"/>
  <text class="page-no" x="11" y="334">5.</text>
  <text class="url" x="436" y="329" text-anchor="end">www.harrowridgepartners.com</text>
</svg>

<!-- Slide 6: closing -->
<svg class="slide slide--closing" viewBox="0 0 455 342">
  <rect width="455" height="342" fill="var(--charcoal)"/>
  <g role="img" aria-label="Photo: hands holding a tablet at a desk">
    <polygon points="0,0 455,0 455,64 0,130" fill="url(#tabletPhoto)"/>
  </g>
  <polygon points="0,130 455,64 455,68 0,134" fill="var(--brand-blue)"/>
  <text class="wordmark wordmark--light" x="228" y="160" text-anchor="middle" font-size="30" letter-spacing=".5">HARROW RIDGE</text>
  <text class="wordmark wordmark--light" x="228" y="178" text-anchor="middle" font-size="11.5" letter-spacing="4">PARTNERS</text>
  <text class="thanks" x="228" y="231" text-anchor="middle" font-size="28">THANK YOU!</text>
  <text class="thanks" x="228" y="253" text-anchor="middle" font-size="16" font-weight="700">for watching!</text>
  <text class="contact" x="211" y="282" text-anchor="end">Street Name, City Name</text>
  <text class="contact" x="211" y="295" text-anchor="end">Zipcode-12345</text>
  <line x1="218" y1="275" x2="218" y2="298" stroke="var(--paper)" stroke-width=".6"/>
  <circle cx="227" cy="280" r="3.2" fill="none" stroke="var(--paper)" stroke-width=".8"/>
  <text class="contact" x="234" y="282">012-345-6789</text>
  <rect x="224" y="290" width="6.5" height="4.5" fill="var(--paper)"/>
  <text class="contact" x="234" y="295">info@harrowridgepartners.com</text>
  <use href="#footer-band" x="0" y="0" width="455" height="342"/>
  <text class="page-no" x="11" y="334">6.</text>
  <text class="url" x="436" y="333" text-anchor="end">www.harrowridgepartners.com</text>
</svg>

</body>
</html>
```